Business Card for new Architectural Firm

I intend to practice in a rural mountain community in upstate NY, focusing on residential and light commercial projects, including second home / vacation properties. I wish to convey a feeling of rural outdoorsy modernity.

Color is important - bold and urbane. Secondary or tertiary colors preferred.

Font is important, idiosyncratic is ok

Optionally, I may choose to use the name Brackenfold Studio. If used as part of your design, all of the Must Haves are still required.

Images uploaded are logos I like

Industry/Entity Type

Residential

Contact Information for Business Card

Lionel Harwicke
Architect (This word should stand alone or be associated with my name - not license number)
NY License No. 052816
lionel@designlhq.com
607 382 9154

Font styles to use
Sans Serif
Decorative

Requirements
Must have
• Whatever files I need to best utilize your design
• PDF
• JPG
• EPS
• Vectorwhatsit
Nice to have
• Logo or element that can be incorporated into other print material.
• Could be a font based card
Should not have
• no clip art
• No templates
• no floor plans
• no building photographs

```html
<!DOCTYPE html>
<html lang="en">
<head>
<meta charset="utf-8">
<title>Lionel Harwicke Architect – Business Card</title>
<link rel="stylesheet" href="https://fonts.googleapis.com/css2?family=Cinzel:wght@500&family=Open+Sans:wght@400&display=swap">
<style>
  :root {
    --page: #e6e6e6;
    --card-front: #ffffff;
    --card-back: #10211f;
    --accent: #0f7c74;
    --accent-deep: #0b5a54;
    --ink: #6f7a79;
    --bark-light: #2fa89c;
    --bark-mid: #137068;
    --bark-dark: #0c2e2b;
  }
  html, body {
    margin: 0;
    padding: 0;
    width: 1200px;
    height: 849px;
    overflow: hidden;
    background: var(--page);
    font-family: "Open Sans", Arial, sans-serif;
  }
  .canvas {
    position: relative;
    width: 1200px;
    height: 849px;
  }
  .card {
    position: absolute;
    top: 270px;
    width: 540px;
    height: 309px;
    box-shadow: 0 6px 18px rgba(0,0,0,0.18);
    box-sizing: border-box;
  }
  .card--back {
    left: 40px;
    background: var(--card-back);
  }
  .card--front {
    left: 620px;
    background: var(--card-front);
  }
  .bark-artwork {
    position: absolute;
    left: 34px;
    top: 26px;
    width: 490px;
    height: 257px;
    border-radius: 4px;
    background: linear-gradient(90deg, var(--bark-dark) 0%, var(--bark-light) 30%, var(--bark-mid) 62%, var(--bark-dark) 100%);
  }
  .brand {
    position: absolute;
    top: 52px;
    right: 40px;
    display: flex;
    align-items: center;
    gap: 12px;
  }
  .brand__mark {
    width: 56px;
    height: 56px;
    background: var(--accent);
  }
  .brand__name {
    margin: 0;
    font-family: "Cinzel", "Times New Roman", serif;
    font-size: 17px;
    line-height: 19px;
    font-weight: 500;
    letter-spacing: 1px;
    text-transform: uppercase;
    color: var(--accent-deep);
  }
  .contact {
    position: absolute;
    left: 40px;
    bottom: 42px;
    margin: 0;
    padding: 0;
    list-style: none;
    font-size: 13px;
    line-height: 22px;
    color: var(--ink);
  }
  .contact__item {
    display: flex;
    align-items: center;
    gap: 12px;
    white-space: nowrap;
  }
  .contact__icon {
    width: 12px;
    height: 12px;
    flex: none;
  }
</style>
</head>
<body>
<main class="canvas">
  <section class="card card--back" aria-label="Card back">
    <div class="bark-artwork" role="img" aria-label="Illustration of birch tree trunks in deep teal tones"></div>
  </section>

  <section class="card card--front" aria-label="Card front">
    <div class="brand">
      <span class="brand__mark" aria-hidden="true"></span>
      <p class="brand__name">Lionel<br>Harwicke<br>Architect</p>
    </div>

    <ul class="contact">
      <li class="contact__item">
        <svg class="contact__icon" viewBox="0 0 12 12" aria-hidden="true">
          <circle cx="6" cy="3.5" r="2.6" fill="#0f7c74"/>
          <path d="M1 12c0-3 2.2-5 5-5s5 2 5 5z" fill="#0f7c74"/>
        </svg>
        <span>Lionel Harwicke | Architect</span>
      </li>
      <li class="contact__item">
        <svg class="contact__icon" viewBox="0 0 12 12" aria-hidden="true">
          <rect x="1" y="1" width="10" height="10" fill="none" stroke="#0f7c74" stroke-width="1.2"/>
          <line x1="3" y1="4.5" x2="9" y2="4.5" stroke="#0f7c74" stroke-width="1"/>
          <line x1="3" y1="7.5" x2="7" y2="7.5" stroke="#0f7c74" stroke-width="1"/>
        </svg>
        <span>NY License No. 052816</span>
      </li>
      <li class="contact__item">
        <svg class="contact__icon" viewBox="0 0 12 12" aria-hidden="true">
          <rect x="3" y="0.5" width="6" height="11" rx="1" fill="none" stroke="#0f7c74" stroke-width="1.2"/>
          <line x1="5" y1="9.5" x2="7" y2="9.5" stroke="#0f7c74" stroke-width="1"/>
        </svg>
        <span>607 382 9154</span>
      </li>
      <li class="contact__item">
        <svg class="contact__icon" viewBox="0 0 12 12" aria-hidden="true">
          <rect x="0.6" y="2.5" width="10.8" height="7.5" fill="none" stroke="#0f7c74" stroke-width="1.2"/>
          <polyline points="0.6,2.5 6,6.8 11.4,2.5" fill="none" stroke="#0f7c74" stroke-width="1.2"/>
        </svg>
        <span>lionel@designlhq.com</span>
      </li>
    </ul>
  </section>
</main>
</body>
</html>
```